Animation (Gif/Lottie file) for a Credit Card Comparison company

We want a GIF or a Lottie file for a Credit Card comparison service that is show when loading. The company is called is Corvanta (www.corvanta-example.com, you can find the brand design online. The GIF/Lottie file should be able to be on repeat as the loading time is between 12 seconds up to 1 minute.

You can use the animation as an inspiration, but follow the guidelines under. Use the copy in the attached file for the steps. They represent:
1) Analyzing your transactions
2) Matching the benefits
3) Preparing your credit card

Font style:
Headers: roc-grotesk-wide, sans-serif
normal text: aktiv-grotesk, sans-serif

Color theme:
Follow the current used on the website.

You can also be creative with the logo or variants of that.

```html
<!DOCTYPE html>
<html lang="en">
<head>
<meta charset="utf-8">
<title>Corvanta loading steps</title>
<link rel="stylesheet" href="https://fonts.googleapis.com/css2?family=Archivo:wdth,wght@125,600&family=Inter:wght@300;400&display=swap">
<style>
  :root {
    --bg: #fcfcfb;
    --ink: #1d2340;
    --accent: #3d5afe;
    --ring: #9a9a9a;
    --dash: #8f8f8f;
    --digit: #3a3a3a;
    --label: #4a4f63;
  }
  html, body {
    margin: 0;
    padding: 0;
    width: 1200px;
    height: 675px;
    overflow: hidden;
    background: var(--bg);
  }
  .loader {
    position: relative;
    width: 1200px;
    height: 675px;
  }
  .brand {
    position: absolute;
    top: 92px;
    left: 0;
    width: 1200px;
    margin: 0;
    display: flex;
    justify-content: center;
    align-items: center;
    gap: 12px;
    font-family: "Archivo", sans-serif;
    font-stretch: 125%;
    font-weight: 600;
    font-size: 26px;
    letter-spacing: 0.5px;
    color: var(--ink);
  }
  .brand-dot {
    width: 12px;
    height: 12px;
    border-radius: 50%;
    background: var(--accent);
  }
  .steps {
    position: absolute;
    inset: 0;
  }
  .step-digit {
    font-family: "Inter", sans-serif;
    font-weight: 300;
    font-size: 42px;
    fill: var(--digit);
    text-anchor: middle;
    dominant-baseline: central;
  }
  .step-active .step-digit { fill: var(--accent); }
  .ring-inner { fill: none; stroke: var(--ring); stroke-width: 1.1; }
  .step-active .ring-inner { stroke: var(--accent); stroke-width: 1.4; }
  .ring-outer { fill: none; stroke: var(--dash); stroke-width: 1.1; stroke-dasharray: 5 4; }
  .connector { stroke: var(--dash); stroke-width: 1.1; stroke-dasharray: 7 5; }
  .step-label {
    position: absolute;
    top: 298px;
    width: 200px;
    margin: 0;
    text-align: center;
    font-family: "Inter", sans-serif;
    font-weight: 400;
    font-size: 15px;
    line-height: 1.4;
    color: var(--label);
  }
  .label-1 { left: 265px; }
  .label-2 { left: 509px; }
  .label-3 { left: 747px; }
</style>
</head>
<body>
  <main class="loader">
    <p class="brand"><span class="brand-dot"></span>Corvanta</p>

    <svg class="steps" width="1200" height="675" viewBox="0 0 1200 675" aria-label="Progress steps 1 to 3">
      <line class="connector" x1="419" y1="240" x2="551" y2="240"/>
      <line class="connector" x1="660" y1="237" x2="792" y2="237"/>

      <g class="step step-active">
        <circle class="ring-outer" cx="365" cy="237" r="41"/>
        <circle class="ring-inner" cx="365" cy="237" r="35"/>
        <text class="step-digit" x="365" y="236">1</text>
      </g>
      <g class="step">
        <circle class="ring-outer" cx="609" cy="236" r="41"/>
        <circle class="ring-inner" cx="609" cy="236" r="35"/>
        <text class="step-digit" x="610" y="235">2</text>
      </g>
      <g class="step">
        <circle class="ring-outer" cx="847" cy="234" r="41"/>
        <circle class="ring-inner" cx="847" cy="234" r="35"/>
        <text class="step-digit" x="848" y="233">3</text>
      </g>
    </svg>

    <p class="step-label label-1">Analyzing your transactions</p>
    <p class="step-label label-2">Matching the benefits</p>
    <p class="step-label label-3">Preparing your credit card</p>
  </main>
</body>
</html>
```